Long Term Insurance for Maturing Women

My business, is a Full service Life and Property Insurance Agency.. I want a reply card, Gloss, with woman showing Maturity, on a beach looking out at a Sun Set, with light Colors of Rainbow.
Thinking: If I am alone, how much income will I need to pay for a Long Term Sickness or Injury. ?
Do I have enough money set aside to cover the added expenses of a long Term Illness ?
Have I enough Life Insurance to cover final expenses, and leave my love ones free of any Debt from my Passing ?
These are real life's concerns, Please Call, let's start finding answers today !
Mark Dunstover, Agent # 0718294 at (714-555-3087) - Halvern Insurance & Financial Service LLC.
Markdun@halverninsx.com 4170 Tamsen Ave, Cypress Ca. 90512

Industry/Entity Type

Business

```html
<!DOCTYPE html>
<html lang="en">
<head>
<meta charset="utf-8">
<title>Long Term Insurance Reply Card</title>
<link rel="stylesheet" href="https://fonts.googleapis.com/css2?family=Cabin:wght@400;500;600&family=Open+Sans:wght@400;500&display=swap">
<style>
  :root {
    --page-bg: #ecebe8;
    --card-white: #fbfbfa;
    --ink: #1c1c1c;
    --white-text: #f4f1ee;
    --bubble-line: #e26fc4;
    --bubble-fill: #ffffff;
    --sky-top: #cfc7c4;
    --sky-mid: #e7c7c5;
    --sky-glow: #f0d3c6;
    --sea-far: #8f99a3;
    --sea-near: #56606a;
    --rock: #2f2b28;
    --stamp-line: #3a3a3a;
    --card-shadow: rgba(0, 0, 0, 0.18);
  }
  * { box-sizing: border-box; margin: 0; padding: 0; }
  html, body { width: 1200px; height: 800px; overflow: hidden; }
  body {
    background: var(--page-bg);
    font-family: "Cabin", "Open Sans", sans-serif;
    color: var(--ink);
  }
  .canvas { position: relative; width: 1200px; height: 800px; }

  .postcard {
    position: absolute;
    top: 230px;
    width: 540px;
    height: 340px;
    box-shadow: 0 4px 14px var(--card-shadow);
    overflow: hidden;
  }
  .postcard--front { left: 40px; }
  .postcard--back { left: 620px; background: var(--card-white); }

  .scene-photo {
    position: absolute; inset: 0;
    background:
      radial-gradient(ellipse 260px 200px at 34% 88%, var(--rock) 0 45%, transparent 70%),
      radial-gradient(ellipse 120px 60px at 40% 47%, var(--sky-glow), transparent 70%),
      linear-gradient(to bottom,
        var(--sky-top) 0%,
        var(--sky-mid) 32%,
        var(--sky-glow) 48%,
        var(--sea-far) 50%,
        var(--sea-near) 100%);
  }

  .thought-bubble {
    position: absolute; left: 150px; top: 6px;
    width: 240px; height: 90px;
  }
  .thought-bubble svg { position: absolute; inset: 0; }
  .thought-bubble__text {
    position: absolute; left: 26px; top: 13px; width: 196px;
    font-family: "Open Sans", sans-serif;
    font-size: 8.6px; line-height: 11px;
    color: var(--ink);
  }

  .concerns {
    position: absolute; left: 250px; top: 112px; width: 272px;
    list-style: none;
    font-family: "Open Sans", sans-serif;
    font-size: 10px; line-height: 13.5px;
    color: var(--ink);
  }
  .concerns li { position: relative; padding-left: 18px; margin-bottom: 2px; }
  .concerns li::before {
    content: ""; position: absolute; left: 0; top: 4px;
    width: 6px; height: 6px; border-radius: 50%; background: var(--ink);
  }

  .call-to-action {
    position: absolute; left: 228px; top: 236px;
    font-family: "Cabin", sans-serif; font-weight: 500;
    font-size: 12px; line-height: 15px;
    color: var(--white-text);
  }

  .stamp-box {
    position: absolute; right: 32px; top: 34px;
    width: 72px; height: 66px;
    border: 1.5px dashed var(--stamp-line);
  }
  .agent-details {
    position: absolute; left: 300px; top: 150px;
    font-family: "Cabin", sans-serif; font-weight: 500;
    font-size: 11px; line-height: 14.5px;
    color: var(--ink);
    font-style: normal;
  }
</style>
</head>
<body>
<main class="canvas">

  <section class="postcard postcard--front">
    <div class="scene-photo" role="img" aria-label="Photograph of a mature woman seated on seaside rocks, looking at a sunset over the ocean beneath a soft pastel rainbow"></div>

    <div class="thought-bubble">
      <svg width="240" height="90" viewBox="0 0 240 90" aria-hidden="true">
        <path d="M20 22 C18 8 48 4 60 10 C74 0 104 2 114 9 C128 0 160 2 170 10 C190 4 222 10 220 24 C236 30 234 54 216 58 C212 70 184 72 170 66 C156 74 124 74 112 68 C98 74 64 74 54 66 C36 72 10 64 14 52 C0 46 4 26 20 22 Z"
              fill="var(--bubble-fill)" stroke="var(--bubble-line)" stroke-width="1.2"/>
        <ellipse cx="52" cy="77" rx="13" ry="5" fill="var(--bubble-fill)" stroke="var(--bubble-line)" stroke-width="1"/>
        <ellipse cx="33" cy="86" rx="8" ry="3" fill="var(--bubble-fill)" stroke="var(--bubble-line)" stroke-width="1"/>
      </svg>
      <p class="thought-bubble__text">If I am alone, how much income will I need to pay for a Long Term Sickness or Injury. ?</p>
    </div>

    <ul class="concerns">
      <li>Do I have enough money set aside to cover the added expenses of a long Term Illness ?</li>
      <li>Have I enough Life Insurance to cover final expenses, and leave my love ones free of any Debt from my Passing ?</li>
    </ul>

    <p class="call-to-action">These are real life's concerns.<br>Please Call, let's start finding answers today !</p>
  </section>

  <section class="postcard postcard--back">
    <div class="stamp-box"></div>
    <address class="agent-details">
      Mark Dunstover<br>
      Agent # 0718294<br>
      (714-555-3087)<br>
      Halvern Insurance &amp; Financial<br>
      Service LLC<br>
      Markdun@halverninsx.com<br>
      4170 Tamsen Ave<br>
      Cypress Ca. 90512
    </address>
  </section>

</main>
</body>
</html>
```